Swimming Pool Service business card needed!!!! Please

Hi Everyone! Thanks for looking at my contest. I PROMISE to provide excellent feedback during this process.

I am starting a new swimming pool cleaning business in San Diego, California and would like your help in making a business card for me.

I like easy to read, classy and sophisticated.

I am having a website designed and I'm looking for it to have pictures of really clean & clear pools.

I really like the blue on white color format, but open to other colors.

I do not have a logo, but the name of my company is GLIMMERWAVE POOL SERVICE.

My tag line is: Pools so clean, you can see yourself "in" them. (does not need to have the quotes around "in"...maybe just italics for this word IN?) You decide for me.

I would like to have a logo designed that incorporates some sort of easy to read letters. I do not want cursive (handwriting) letters. I thought about having a "reflection" of letters (mirror image), but think that this will be hard to read from far away. Maybe you can surprise me and come up with an idea that works using the a mirror image....but I'm not sure. I was leaning toward plain old BLOCK letters as I think it would be easy to read on my truck.

I would like to have the NWTBG and HML logos on the back of the card. I have attached those two as files. You can put other things on the back as well, but I need these two logos on there. Or maybe put them on the front of the card if you have a better idea for the back of the card! :-)

Maybe blue on the back of the card and white on the front of the card? I don't know, I'm just thinking out loud.

I had another card done awhile ago called TALLGRASS SHIRTS. I have uploaded a copy of that card for your reference. I don't want this card to be the same as my new company is a swimming pool cleaning company, but I wanted you to see what I liked in the past.

THANK YOU!!!!

Reason: Partner out of town and want their feedback....so need more time to decide and designs still coming in.

Industry/Entity Type

Business

Contact Information for Business Card

GLIMMERWAVE POOL SERVICE
Rick Velund
Owner
8142 Palo Brinco Ave. #219
San Diego, CA 92587
858-291-6037
www.glimmerwavepoolservice.example

Font styles to use
Sans Serif

Colors
0255a3
3176b5
ffffff

Requirements
Nice to have
• Some things to (possibly) add to back of card (in no particular order)
• HML logo
• NWTBG logo
• Free Estimates
• Residential and Commercial Services
• Equipment Repairs
• Saltwater Systems
• Licensed, Bonded, Insured
• Family Owned and Operated
• No Contracts
• =======================
• Check out the FlexMark business card that i attached.
• i think they did this using a chrome overlay.
• Can any of you guys design that? or is that done at my printer?
• ==================
Should not have
• Hi Designers-
• The first round of cards came back and let's stay away from the light blue (powder blue) color. I don't like the look of it on the business cards.
• Also, the pool company JPG's that I attached are other logos of pool companies that I liked. I don't want them to be on my card. The only logos that should be on my card are the one you are going to come up with for my company, the HML logo and the NWTBG logo.
• Lastly, no vertical cards and no split cards (logo on left, contact info on right side).
• Thanks much!

```html
<!DOCTYPE html>
<html lang="en">
<head>
<meta charset="utf-8">
<title>Glimmerwave Pool Service – Business Card</title>
<link rel="stylesheet" href="https://fonts.googleapis.com/css2?family=Montserrat:ital,wght@0,300;0,400;0,500;0,600;0,700;1,600&display=swap">
<style>
  :root {
    --stage: #e9eaec;
    --card-blue: #1b84c6;
    --icon-bg: #e8f1f8;
    --icon-ink: #1b84c6;
    --ink-white: #ffffff;
    --ink-soft: #d9ebf7;
    --ink-dark: #1c2330;
    --brand-blue: #0255a3;
    --badge-a: #3176b5;
    --badge-b: #c8383b;
    --card-white: #ffffff;
  }
  * { box-sizing: border-box; margin: 0; padding: 0; }
  html, body {
    width: 1200px; height: 675px; overflow: hidden;
    background: var(--stage);
    font-family: "Montserrat", Arial, sans-serif;
  }
  .canvas { position: relative; width: 1200px; height: 675px; }
  .card {
    position: absolute; top: 210px; width: 394px; height: 240px;
    box-shadow: 0 2px 6px rgba(0,0,0,.18);
    overflow: hidden;
  }
  .card--front { left: 204px; background: var(--card-blue); color: var(--ink-white); }
  .card--back { left: 619px; background: var(--card-white); }

  .tagline { position: absolute; left: 12px; top: 10px; display: flex; gap: 6px; }
  .tagline__mark { font-size: 34px; font-weight: 700; line-height: 0.9; }
  .tagline__text {
    font-size: 7.5px; font-weight: 600; font-style: italic;
    text-transform: uppercase; line-height: 1.55; letter-spacing: .3px; margin-top: 3px;
  }

  .identity { position: absolute; left: 166px; top: 54px; }
  .identity__name { font-size: 25px; font-weight: 300; letter-spacing: .3px; white-space: nowrap; }
  .identity__name strong { font-weight: 700; }
  .identity__role { font-size: 9.5px; font-weight: 400; color: var(--ink-soft); margin-top: 3px; }

  .contact { position: absolute; left: 166px; right: 10px; top: 121px; list-style: none; }
  .contact__item { display: flex; align-items: flex-start; gap: 9px; margin-bottom: 9px; font-size: 12.5px; font-weight: 500; }
  .contact__icon {
    width: 19px; height: 19px; border-radius: 50%; background: var(--icon-bg);
    display: flex; align-items: center; justify-content: center; flex: none;
  }
  .contact__text { line-height: 19px; white-space: nowrap; }
  .contact__text--web { font-size: 10px; font-weight: 700; letter-spacing: -0.1px; }
  .contact__text--web .contact__tld { font-weight: 400; }
  .contact__text--address { font-weight: 400; line-height: 1.35; margin-top: 1px; }

  .brand { position: absolute; left: 56px; top: 80px; color: var(--ink-dark); font-weight: 700; }
  .brand__line { font-size: 24px; letter-spacing: .3px; line-height: 1.05; white-space: nowrap; }

  .badges { position: absolute; right: 16px; bottom: 16px; display: flex; gap: 10px; }
  .badge { width: 32px; height: 32px; border-radius: 50%; }
  .badge--nwtbg { background: var(--badge-a); }
  .badge--hml { background: var(--badge-b); }
</style>
</head>
<body>
<main class="canvas">
  <section class="card card--front" aria-label="Card front">
    <div class="tagline">
      <span class="tagline__mark">“</span>
      <p class="tagline__text">Pools so clean,<br>you can see yourself<br>‘in’ them</p>
    </div>

    <div class="identity">
      <h1 class="identity__name"><strong>RICK</strong> Velund</h1>
      <p class="identity__role">OWNER/FOUNDER</p>
    </div>

    <ul class="contact">
      <li class="contact__item">
        <span class="contact__icon">
          <svg width="11" height="11" viewBox="0 0 24 24" aria-hidden="true"><path fill="var(--icon-ink)" d="M6.6 10.8a15.1 15.1 0 0 0 6.6 6.6l2.2-2.2c.3-.3.7-.4 1-.2 1.1.4 2.3.6 3.6.6.6 0 1 .4 1 1V20c0 .6-.4 1-1 1A17 17 0 0 1 3 4c0-.6.4-1 1-1h3.5c.6 0 1 .4 1 1 0 1.3.2 2.5.6 3.6.1.3 0 .7-.2 1z"/></svg>
        </span>
        <span class="contact__text">92587 858-291-6037</span>
      </li>
      <li class="contact__item">
        <span class="contact__icon">
          <svg width="11" height="11" viewBox="0 0 24 24" aria-hidden="true"><g fill="none" stroke="var(--icon-ink)" stroke-width="2"><circle cx="12" cy="12" r="9"/><path d="M3 12h18M12 3c3 3 3 15 0 18M12 3c-3 3-3 15 0 18"/></g></svg>
        </span>
        <span class="contact__text contact__text--web">glimmerwavepoolservice<span class="contact__tld">.example</span></span>
      </li>
      <li class="contact__item">
        <span class="contact__icon">
          <svg width="11" height="11" viewBox="0 0 24 24" aria-hidden="true"><path fill="var(--icon-ink)" d="M12 3 2 12h3v9h5v-6h4v6h5v-9h3z"/></svg>
        </span>
        <span class="contact__text contact__text--address">8142 Palo Brinco Ave.<br>#219 San Diego, CA</span>
      </li>
    </ul>
  </section>

  <section class="card card--back" aria-label="Card back">
    <div class="brand">
      <p class="brand__line">GLIMMERWAVE</p>
      <p class="brand__line">POOL SERVICE</p>
    </div>
    <div class="badges">
      <span class="badge badge--nwtbg" role="img" aria-label="NWTBG membership badge"></span>
      <span class="badge badge--hml" role="img" aria-label="HML certification badge"></span>
    </div>
  </section>
</main>
</body>
</html>
```